RIVERSTONE PAVING & EARTHWORKS

I would like the front of the card to have my logo centred.
I need it to have my contact details on the back of the card which are: RiverstonePavingEarthworks@mailbrook.net
0439268417
and a Facebook icon

```html
<!DOCTYPE html>
<html lang="en">
<head>
<meta charset="utf-8">
<title>Riverstone Paving &amp; Earthworks — Business Card</title>
<link rel="stylesheet" href="https://fonts.googleapis.com/css2?family=Poppins:wght@300;700&display=swap">
<style>
  :root {
    --page-bg: #2b3036;
    --card-black: #050505;
    --card-panel: #111214;
    --edge-cyan: #1fa3e0;
    --edge-navy: #1f3f9a;
    --brand-blue: #2389e0;
    --text-light: #d7d9dc;
    --text-muted: #8e9297;
  }
  * { box-sizing: border-box; margin: 0; padding: 0; }
  html, body { width: 1200px; height: 985px; overflow: hidden; }
  body {
    background: var(--page-bg);
    font-family: "Poppins", sans-serif;
    position: relative;
  }
  .card {
    position: absolute;
    border-radius: 24px;
    background: var(--card-black);
    border: 3px solid var(--edge-cyan);
    box-shadow: 0 0 0 3px var(--edge-navy), 0 24px 50px rgba(0,0,0,.55);
    overflow: hidden;
  }
  /* Back: contact side, portrait */
  .card-back { left: 70px; top: 150px; width: 380px; height: 665px; }
  .back-decoration {
    position: absolute; left: 40px; top: 150px; width: 300px; height: 340px;
    background: radial-gradient(ellipse at center, #141517 0%, #0b0b0c 70%, var(--card-black) 100%);
    border-radius: 12px;
  }
  .back-content {
    position: absolute; left: 0; right: 0; top: 180px;
    display: flex; flex-direction: column; align-items: center;
    padding: 0 28px;
  }
  .brand-mark {
    display: flex; align-items: center; gap: 10px;
    color: var(--brand-blue); font-weight: 700;
    text-align: center; line-height: 1.15;
  }
  .brand-mark .brand-square {
    flex: none; width: 16px; height: 16px; background: var(--brand-blue);
  }
  .card-back .brand-mark { font-size: 20px; }
  .divider {
    width: 240px; height: 2px; margin: 26px 0 24px;
    background: linear-gradient(90deg, var(--edge-cyan), var(--edge-navy));
  }
  .contact-list { list-style: none; width: 100%; }
  .contact-item {
    display: flex; align-items: center; gap: 8px;
    color: var(--text-light); font-weight: 300; font-size: 12.5px;
    margin-bottom: 14px; white-space: nowrap;
  }
  .contact-item svg { flex: none; }
  .social-item { color: var(--text-muted); }
  .social-square {
    width: 22px; height: 22px; border-radius: 3px;
    background: linear-gradient(135deg, var(--edge-cyan), var(--edge-navy));
  }
  /* Front: logo side, landscape */
  .card-front { left: 510px; top: 300px; width: 640px; height: 366px; }
  .front-pattern {
    position: absolute; inset: 0;
    background: radial-gradient(ellipse at center, #1a1b1d 0%, #101112 60%, #090909 100%);
  }
  .front-content {
    position: absolute; inset: 0;
    display: flex; align-items: center; justify-content: center;
  }
  .card-front .brand-mark { font-size: 30px; }
</style>
</head>
<body>
  <section class="card card-back" aria-label="Card back with contact details">
    <div class="back-decoration" role="img" aria-label="Large faint brand emblem decoration"></div>
    <div class="back-content">
      <div class="brand-mark">
        <span class="brand-square"></span>
        <span class="brand-name">RIVERSTONE PAVING<br>&amp; EARTHWORKS</span>
      </div>
      <div class="divider"></div>
      <ul class="contact-list">
        <li class="contact-item">
          <svg width="14" height="11" viewBox="0 0 14 11" aria-hidden="true">
            <rect x="0.5" y="0.5" width="13" height="10" rx="1" fill="none" stroke="#2389e0"/>
            <path d="M1 1 L7 6 L13 1" fill="none" stroke="#2389e0"/>
          </svg>
          <span>RiverstonePavingEarthworks@mailbrook.net</span>
        </li>
        <li class="contact-item">
          <svg width="12" height="14" viewBox="0 0 12 14" aria-hidden="true">
            <rect x="1" y="0.5" width="10" height="13" rx="2" fill="none" stroke="#2389e0"/>
            <line x1="5" y1="11" x2="7" y2="11" stroke="#2389e0"/>
          </svg>
          <span>0439268417</span>
        </li>
        <li class="contact-item social-item">
          <span class="social-square"></span>
          <span>RiverstonePaving</span>
        </li>
      </ul>
    </div>
  </section>

  <section class="card card-front" aria-label="Card front with centred brand">
    <div class="front-pattern" role="img" aria-label="Repeating brand emblem pattern in dark grey"></div>
    <div class="front-content">
      <div class="brand-mark">
        <span class="brand-square"></span>
        <span class="brand-name">RIVERSTONE PAVING<br>&amp; EARTHWORKS</span>
      </div>
    </div>
  </section>
</body>
</html>
```